Ridgeway Framers Business Card

I'm looking for a business card design for a start-up Handyman/Construction Company. The organization will double as a ministry to the homeless, hoping to create job opportunity and training to the homeless, providing a pathway back to being "homed". I'm looking for a simple to "seeming" simple design. Open to all thoughts.

Industry/Entity Type

Ministry

Requirements
Must have
• Logo (Attached), Name, Phone, Email and Address. Note - "*Registered and Insured".

```html
<!DOCTYPE html>
<html lang="en">
<head>
<meta charset="utf-8">
<title>Ridgeway Framers Business Card</title>
<link rel="stylesheet" href="https://fonts.googleapis.com/css2?family=Open+Sans:wght@400;600;700&display=swap">
<style>
  :root {
    --backdrop: #e4e5e7;
    --card: #ffffff;
    --navy: #25344f;
    --ink: #2b2f36;
    --plum: #7d2a80;
  }
  * { margin: 0; padding: 0; box-sizing: border-box; }
  html, body {
    width: 1200px;
    height: 900px;
    overflow: hidden;
    background: var(--backdrop);
    font-family: "Open Sans", Arial, sans-serif;
  }
  .stage {
    width: 1200px;
    height: 900px;
    display: flex;
    align-items: center;
    justify-content: center;
  }
  .business-card {
    width: 840px;
    height: 480px;
    background: var(--card);
    border-radius: 24px;
    box-shadow: 0 6px 24px rgba(0, 0, 0, 0.12);
    display: flex;
    flex-direction: column;
    align-items: center;
    padding-top: 118px;
  }
  .company-name {
    font-size: 60px;
    font-weight: 700;
    color: var(--navy);
    letter-spacing: 1px;
    line-height: 1;
  }
  .contact-block {
    margin-top: 74px;
    text-align: center;
    font-size: 21px;
    font-weight: 400;
    color: var(--ink);
    line-height: 1.3;
  }
  .divider {
    width: 560px;
    height: 2px;
    background: var(--plum);
    margin-top: 10px;
  }
  .credentials {
    margin-top: 16px;
    font-size: 24px;
    font-weight: 600;
    color: var(--navy);
  }
</style>
</head>
<body>
  <main class="stage">
    <section class="business-card">
      <h1 class="company-name">Ridgeway Framers</h1>
      <address class="contact-block" style="font-style: normal;">
        <p class="contact-address">Your Address</p>
        <p class="contact-phone">000 123 456</p>
        <p class="contact-email">youremail@domain.com</p>
      </address>
      <div class="divider"></div>
      <p class="credentials">Registered and Insured</p>
    </section>
  </main>
</body>
</html>
```